Bench Advertisement - We Buy Houses Design Needed

Need a catchy, simple but elegant design for bus benches to advertise our company.

We need our website, or phone number, and a smal description (1-2 bulletpoints of what we do and what we offer)

The tricky part is for the designer to fit everything and make the website name as part of the title and fitting everything so that people passing by on the street can see what we offer.

Our website is quickhomeofferhub.com - (916) 555-0142

Something simple but something that catches the eye of walking pedestrians, and drivers driving by the bench.

Our company buys houses, any condition, any situation, we buy houses for cash and close quickly. You can use this description to create a few bulletpoints however you like. Must follow dimensions in attachment.

Target Market(s)

People in foreclosure, about to lose their homes, people that need a quick cash sale of their property

Industry/Entity Type

Real Estate

Requirements
Must have
• catchy, website name, phone number, few brief bulletpoints about what we offer, colors that will catch peoples eye while walking or driving - advertisement will be placed on bus benches - visit our website to see the type of houses we buy - Also have more work for winner of design with possible bonuses
Nice to have
• Feel free to use description or images on our website - make sure the description is just bullet points and it fits with the overall theme / size of the advertisement - Bold bright colors - put yourself in their shoes (if you were going through financial difficulties and about to lose your house to foreclosure or auction, what would you want to see to pick up the phone and call us for a quick sale of your house?) (or if you have a house that you are having a problem with, problem renters, unkept/beat up house, what would make you want to call us and sell your house to us?)

```html
<!DOCTYPE html>
<html lang="en">
<head>
<meta charset="utf-8">
<title>Quick Home Offer Hub – Bench Advertisement</title>
<link rel="stylesheet" href="https://fonts.googleapis.com/css2?family=Open+Sans:wght@400;600;700&family=PT+Sans+Narrow:wght@700&display=swap">
<style>
  :root {
    --teal-dark: #3e8b96;
    --teal-light: #74b8c1;
    --orange: #f07a16;
    --label-grey: #7a7a7a;
    --rule-grey: #9a9a9a;
    --white: #ffffff;
    --stage: #ececec;
  }
  * { margin: 0; padding: 0; box-sizing: border-box; }
  html, body { width: 1200px; height: 768px; overflow: hidden; }
  body { background: var(--stage); font-family: "Open Sans", sans-serif; }

  .bench-ad {
    position: absolute; left: 0; top: 217px;
    width: 1200px; height: 334px;
    background: var(--white); overflow: hidden;
  }
  .bands { position: absolute; inset: 0; }

  .steps-title {
    position: absolute; left: 0; width: 656px; top: 30px;
    text-align: center; color: var(--orange);
    font-weight: 600; font-size: 30px; letter-spacing: -0.3px;
  }
  .step-label {
    position: absolute; top: 184px; width: 150px; margin-left: -75px;
    text-align: center; font-size: 10px; line-height: 11px;
    color: var(--label-grey); text-transform: uppercase;
  }

  .brand-name {
    position: absolute; left: 720px; width: 470px; top: 150px;
    text-align: center; color: var(--teal-dark);
    font-weight: 400; font-size: 28px; text-transform: uppercase;
  }

  .offer-list {
    position: absolute; left: 36px; top: 257px; list-style: none;
    font-family: "PT Sans Narrow", sans-serif; font-weight: 700;
    font-size: 23px; line-height: 29px; color: var(--white);
    text-transform: uppercase;
  }
  .offer-list li { display: flex; align-items: center; gap: 12px; }
  .offer-list li::before {
    content: ""; width: 14px; height: 14px;
    background:
      linear-gradient(var(--white),var(--white)) 0 0/6px 6px no-repeat,
      linear-gradient(var(--white),var(--white)) 8px 0/6px 6px no-repeat,
      linear-gradient(var(--white),var(--white)) 0 8px/6px 6px no-repeat,
      linear-gradient(var(--white),var(--white)) 8px 8px/6px 6px no-repeat;
  }

  .contact {
    position: absolute; right: 32px; top: 226px; text-align: right;
    color: var(--white);
  }
  .contact-phone { font-weight: 700; font-size: 50px; line-height: 58px; letter-spacing: -0.5px; }
  .contact-web { font-weight: 600; font-size: 25px; line-height: 30px; text-transform: uppercase; }
</style>
</head>
<body>
  <section class="bench-ad">
    <svg class="bands" width="1200" height="334" viewBox="0 0 1200 334">
      <defs>
        <linearGradient id="tealFill" x1="0" y1="0" x2="0" y2="1">
          <stop offset="0" stop-color="var(--teal-light)"/>
          <stop offset="1" stop-color="var(--teal-dark)"/>
        </linearGradient>
        <linearGradient id="iconFill" x1="0" y1="0" x2="0" y2="1">
          <stop offset="0" stop-color="#5aa7b1"/>
          <stop offset="1" stop-color="#347f8a"/>
        </linearGradient>
      </defs>

      <!-- bottom bands -->
      <path class="offer-band" d="M0 241 H668 L568 334 H0 Z" fill="url(#tealFill)"/>
      <path class="contact-band" d="M715 216 H1200 V334 H588 Z" fill="url(#tealFill)"/>

      <!-- step connector -->
      <g class="step-connector" fill="none" stroke="var(--rule-grey)" stroke-width="2">
        <path d="M329 75 V91"/>
        <path d="M85 107 V91 H576 V107"/>
        <path d="M249 91 V107 M412 91 V107"/>
      </g>

      <!-- step icons -->
      <g class="step-icons">
        <circle cx="84" cy="147" r="31" fill="url(#iconFill)"/>
        <g fill="none" stroke="#fff" stroke-width="1.8">
          <rect x="73" y="136" width="20" height="22" rx="2"/>
          <path d="M77 142 H89 M77 147 H89 M77 152 H84"/>
          <path d="M87 160 L96 149" stroke-width="2.4"/>
        </g>

        <circle cx="248" cy="147" r="31" fill="url(#iconFill)"/>
        <path d="M238 141 c0 -4 3 -6 5 -6 l3 5 -3 3 c1 4 4 7 8 8 l3 -3 5 3 c0 2 -2 5 -6 5 c-9 -1 -15 -7 -15 -15 Z" fill="#fff"/>
        <path d="M252 135 L258 141 M252 141 L258 135 M254 135 H258 V139" stroke="#fff" stroke-width="1.6" fill="none"/>

        <circle cx="411" cy="147" r="31" fill="url(#iconFill)"/>
        <g fill="none" stroke="#fff" stroke-width="1.8" stroke-linejoin="round">
          <rect x="398" y="144" width="6" height="14"/>
          <path d="M404 145 L410 136 c2 -2 4 -1 4 2 l-1 5 h8 c2 0 3 2 2 4 l-3 9 c-1 2 -2 2 -4 2 h-10"/>
        </g>

        <circle cx="575" cy="147" r="31" fill="url(#iconFill)"/>
        <path d="M562 148 L575 136 L588 148 H584 V159 H578 V152 H572 V159 H566 V148 Z" fill="#fff"/>
        <rect x="582" y="137" width="3" height="7" fill="#fff"/>
      </g>
    </svg>

    <h2 class="steps-title">WE MAKE IT SIMPLE</h2>
    <p class="step-label" style="left:84px">Fill out the form</p>
    <p class="step-label" style="left:248px">We'll call you within a few hours</p>
    <p class="step-label" style="left:411px">We work with you on a solution</p>
    <p class="step-label" style="left:575px">Move on with your life</p>

    <h1 class="brand-name">Quick Home Offer Hub</h1>

    <ul class="offer-list">
      <li>Our company buys houses, any condition, any situation</li>
      <li>We buy houses for cash &amp; close quickly</li>
    </ul>

    <div class="contact">
      <p class="contact-phone">Cell (916) 555-0142</p>
      <p class="contact-web">quickhomeofferhub.com</p>
    </div>
  </section>
</body>
</html>
```